PLINOVERT Multistep design - needs to match our existing design.

We have a multistep form(7 pages) we need the design for (rest of the website is done).
The multistep form is a vital part of the website, as it is the main service - so the form design should fit into the rest of the site.
Please take a look at the attached file - all about colors, fonts etc. is included in the file.

Target Market(s)

People looking for an interior architect in Denmark

Industry/Entity Type

Interior Design

Number of Pages Required

1 page

Requirements
Nice to have
• It's attached in the pdf file

```html
<!DOCTYPE html>
<html lang="en">
<head>
<meta charset="utf-8">
<title>PLINOVERT – Rooms Details</title>
<link href="https://fonts.googleapis.com/css2?family=Raleway:wght@500;600;700&display=swap" rel="stylesheet">
<style>
  :root {
    --scene-dark: #24292d;
    --scene-mid: #3d4347;
    --scene-light: #6a6c6b;
    --panel: rgba(112, 120, 126, 0.55);
    --panel-edge: rgba(255, 255, 255, 0.08);
    --field: #ffffff;
    --ink: #33393d;
    --ink-soft: #5a6166;
    --on-dark: #ffffff;
    --toggle-track: #3a4044;
  }
  * { box-sizing: border-box; margin: 0; padding: 0; }
  html, body { width: 1200px; height: 675px; overflow: hidden; }
  body { font-family: "Raleway", sans-serif; background: var(--scene-dark); }

  .screen { position: relative; width: 1200px; height: 675px; overflow: hidden; }

  .backdrop {
    position: absolute; inset: 0;
    background:
      radial-gradient(ellipse 40% 30% at 82% 35%, rgba(190,170,150,0.35), transparent 70%),
      radial-gradient(ellipse 50% 40% at 20% 70%, rgba(150,150,145,0.25), transparent 70%),
      linear-gradient(160deg, var(--scene-mid) 0%, var(--scene-dark) 45%, var(--scene-light) 100%);
  }

  .form-panel {
    position: absolute; left: 242px; top: 79px; width: 717px; height: 510px;
    background: var(--panel);
    border: 1px solid var(--panel-edge);
    backdrop-filter: blur(2px);
  }

  .form-title {
    position: absolute; left: 18px; top: 38px;
    color: var(--on-dark); font-size: 17px; font-weight: 700;
  }
  .form-step {
    position: absolute; left: 18px; top: 61px;
    color: var(--on-dark); font-size: 10px; font-weight: 500;
  }

  .whole-house {
    position: absolute; right: 91px; top: 44px;
    display: flex; align-items: center; gap: 14px;
    color: var(--on-dark); font-size: 12px; font-weight: 600;
  }
  .toggle {
    width: 46px; height: 19px; border-radius: 10px;
    background: var(--toggle-track); border: 2px solid var(--field);
    position: relative;
  }
  .toggle::after {
    content: ""; position: absolute; left: 2px; top: 1px;
    width: 13px; height: 13px; border-radius: 50%; background: var(--field);
  }

  .room-select {
    position: absolute; width: 254px; height: 33px;
    background: var(--field); border-radius: 2px;
    display: flex; align-items: center; padding: 0 10px;
    color: var(--ink); font-size: 11px; font-weight: 600;
  }
  .room-select .room-icon { width: 18px; height: 18px; margin-right: 10px; flex: none; }
  .room-select .room-name { flex: 1; }
  .room-select .chevron { width: 10px; height: 10px; flex: none; }

  .col-left { left: 91px; }
  .col-right { left: 368px; }
  .col-center { left: 230px; }

  .actions {
    position: absolute; top: 469px; left: 240px;
    display: flex; gap: 10px;
  }
  .btn {
    height: 32px; background: var(--field); color: var(--ink);
    border: none; font-family: inherit; font-size: 10px; font-weight: 700;
    letter-spacing: 0.5px; text-transform: uppercase;
  }
  .btn-back { width: 113px; }
  .btn-view { width: 112px; }

  svg .line { fill: none; stroke: var(--ink-soft); stroke-width: 1.4; stroke-linecap: round; stroke-linejoin: round; }
</style>
</head>
<body>
<main class="screen">
  <div class="backdrop" role="img" aria-label="Blurred photo of an architect's desk with rolled plans and paperwork"></div>

  <svg width="0" height="0" style="position:absolute">
    <defs>
      <symbol id="chevron" viewBox="0 0 10 10"><path class="line" d="M2 3.5 L5 6.5 L8 3.5" style="stroke:var(--ink);stroke-width:1.6"/></symbol>
      <symbol id="icon-kids" viewBox="0 0 18 18"><rect class="line" x="2" y="2" width="14" height="14" rx="1"/><circle class="line" cx="9" cy="7" r="2.5"/><path class="line" d="M5 15 Q9 9 13 15"/></symbol>
      <symbol id="icon-bed" viewBox="0 0 18 18"><path class="line" d="M2 5 V15 M2 12 H16 V15 M2 9 H16 V12"/><rect class="line" x="4" y="6.5" width="3" height="2.5"/></symbol>
      <symbol id="icon-office" viewBox="0 0 18 18"><path class="line" d="M2 10 H16 M4 10 V15 M14 10 V15"/><rect class="line" x="6" y="4" width="6" height="4"/></symbol>
      <symbol id="icon-living" viewBox="0 0 18 18"><path class="line" d="M3 8 V14 H15 V8 M5 11 H13 M5 8 V11 M13 8 V11 M4 5 H14"/></symbol>
      <symbol id="icon-kitchen" viewBox="0 0 18 18"><rect class="line" x="2" y="4" width="14" height="11"/><path class="line" d="M2 8 H16 M9 8 V15"/><circle class="line" cx="5.5" cy="6" r="0.8"/></symbol>
      <symbol id="icon-dining" viewBox="0 0 18 18"><circle class="line" cx="9" cy="9" r="6.5"/><circle class="line" cx="9" cy="9" r="3.5"/></symbol>
      <symbol id="icon-utility" viewBox="0 0 18 18"><rect class="line" x="3" y="2" width="12" height="14" rx="1"/><circle class="line" cx="9" cy="10" r="3.5"/><path class="line" d="M3 5 H15"/></symbol>
      <symbol id="icon-entrance" viewBox="0 0 18 18"><rect class="line" x="5" y="2" width="8" height="14"/><circle class="line" cx="11" cy="9" r="0.6"/></symbol>
      <symbol id="icon-bath" viewBox="0 0 18 18"><path class="line" d="M3 16 V3 H7 M3 9 H15 V12 Q15 15 12 15 H6 M11 3 V6"/></symbol>
      <symbol id="icon-basement" viewBox="0 0 18 18"><path class="line" d="M3 15 H6 V12 H9 V9 H12 V6 H15"/></symbol>
      <symbol id="icon-patio" viewBox="0 0 18 18"><path class="line" d="M3 16 V6 H8 V16 M8 10 H15 V16 M5 3 V6"/></symbol>
      <symbol id="icon-outdoor" viewBox="0 0 18 18"><path class="line" d="M2 6 H16 M2 12 H16 M4 3 V16 M8 3 V16 M12 3 V16 M15 3 V16"/></symbol>
      <symbol id="icon-hobby" viewBox="0 0 18 18"><path class="line" d="M9 2 V9 M6 5 Q9 8 12 5 M9 9 L6 16 M9 9 L12 16"/></symbol>
    </defs>
  </svg>

  <section class="form-panel" aria-labelledby="rooms-title">
    <h1 class="form-title" id="rooms-title">Rooms Details</h1>
    <p class="form-step">Step 3 of 3</p>

    <div class="whole-house">Whole House <span class="toggle" aria-hidden="true"></span></div>

    <div class="room-select col-left" style="top:95px"><svg class="room-icon"><use href="#icon-kids"/></svg><span class="room-name">Children's Room</span><svg class="chevron"><use href="#chevron"/></svg></div>
    <div class="room-select col-right" style="top:95px"><svg class="room-icon"><use href="#icon-bed"/></svg><span class="room-name">Bedroom</span><svg class="chevron"><use href="#chevron"/></svg></div>

    <div class="room-select col-left" style="top:142px"><svg class="room-icon"><use href="#icon-office"/></svg><span class="room-name">Office</span><svg class="chevron"><use href="#chevron"/></svg></div>
    <div class="room-select col-right" style="top:142px"><svg class="room-icon"><use href="#icon-living"/></svg><span class="room-name">Living Room</span><svg class="chevron"><use href="#chevron"/></svg></div>

    <div class="room-select col-left" style="top:188px"><svg class="room-icon"><use href="#icon-kitchen"/></svg><span class="room-name">Kitchen</span><svg class="chevron"><use href="#chevron"/></svg></div>
    <div class="room-select col-right" style="top:188px"><svg class="room-icon"><use href="#icon-dining"/></svg><span class="room-name">Dinning Area</span><svg class="chevron"><use href="#chevron"/></svg></div>

    <div class="room-select col-left" style="top:235px"><svg class="room-icon"><use href="#icon-utility"/></svg><span class="room-name">Utility Room</span><svg class="chevron"><use href="#chevron"/></svg></div>
    <div class="room-select col-right" style="top:235px"><svg class="room-icon"><use href="#icon-entrance"/></svg><span class="room-name">Entrance Hall</span><svg class="chevron"><use href="#chevron"/></svg></div>

    <div class="room-select col-left" style="top:282px"><svg class="room-icon"><use href="#icon-bath"/></svg><span class="room-name">Bathroom</span><svg class="chevron"><use href="#chevron"/></svg></div>
    <div class="room-select col-right" style="top:282px"><svg class="room-icon"><use href="#icon-basement"/></svg><span class="room-name">Basement</span><svg class="chevron"><use href="#chevron"/></svg></div>

    <div class="room-select col-left" style="top:328px"><svg class="room-icon"><use href="#icon-patio"/></svg><span class="room-name">Patio</span><svg class="chevron"><use href="#chevron"/></svg></div>
    <div class="room-select col-right" style="top:328px"><svg class="room-icon"><use href="#icon-outdoor"/></svg><span class="room-name">Outdoor</span><svg class="chevron"><use href="#chevron"/></svg></div>

    <div class="room-select col-center" style="top:375px"><svg class="room-icon"><use href="#icon-hobby"/></svg><span class="room-name">Hobby Room</span><svg class="chevron"><use href="#chevron"/></svg></div>

    <div class="actions">
      <button class="btn btn-back" type="button">Back</button>
      <button class="btn btn-view" type="button">View Matches</button>
    </div>
  </section>
</main>
</body>
</html>
```